Web Design for a Travel Industry Company

i am Looking for a Web designer, that's makes me a template for our company in the Travel Sector. It must have a booking tool and a tool for queries. Pictures come from us. It must be simple so that we can then organize further. We plan a cover side, than in the top line, we want have buttons for choose. perfect will be a mix from the hotel Wendtner homepage in Vienna and Pammerlstein.at. The site is already purchased and owned by us.
Updates

Ich brauche zusätzliche Tage um durchzusehen

Target Market(s)

Travel Industry / Luxury and GAY Peopele

Logo Text

see the Logos

Requirements
Must have
• is for gays. The design should be customized.
Nice to have
• For the website a booking tools. We can deliver pic from Vienna for the Web design.

```html
<!DOCTYPE html>
<html lang="en">
<head>
<meta charset="utf-8">
<title>Prism Voyages — Travel</title>
<link href="https://fonts.googleapis.com/css2?family=Open+Sans:wght@600;700;800&family=Raleway:wght@400;500;600&display=swap" rel="stylesheet">
<style>
:root{
  --orange:#f08a24;
  --purple:#6a1b78;
  --ink:#161616;
  --muted:#555;
  --panel:#e2e8ef;
  --footer:#9d96c6;
  --footer-dark:#2b1f6e;
  --white:#fff;
}
*{box-sizing:border-box;margin:0;padding:0}
html,body{width:1200px;height:3274px;overflow:hidden}
body{position:relative;background:var(--white);font-family:"Raleway",sans-serif;color:var(--ink)}
.abs{position:absolute}
.photo{position:absolute}
h2{font-family:"Open Sans",sans-serif;font-weight:700;font-size:16px;letter-spacing:.2px;text-transform:uppercase;color:var(--ink)}
p.body{font-size:10.5px;line-height:18px;color:var(--muted)}

/* hero */
.hero{left:0;top:0;width:1200px;height:610px;background:linear-gradient(180deg,#3b3a44 0%,#6a6a6e 35%,#8a8780 55%,#3a3630 72%,#2d2c33 100%)}
.brand{left:86px;top:38px;display:flex;align-items:center;gap:10px}
.brand-dot{width:44px;height:44px;border-radius:50%;background:var(--white)}
.brand-name{font-family:"Open Sans",sans-serif;font-weight:700;font-size:18px;color:var(--white)}
.nav{right:88px;top:30px;display:flex;gap:34px;list-style:none}
.nav li{font-family:"Open Sans",sans-serif;font-size:10.5px;font-weight:600;color:var(--orange);text-transform:uppercase}
.book{left:1031px;top:79px;width:86px;height:27px;border-radius:14px;background:var(--orange);color:var(--white);font-family:"Open Sans",sans-serif;font-weight:700;font-size:11px;display:flex;align-items:center;justify-content:center}
.search{left:338px;top:295px;width:524px;height:60px;border-radius:30px;background:rgba(220,220,215,.85);display:flex;align-items:center}
.search .select{width:136px;height:100%;display:flex;align-items:center;justify-content:center;gap:6px;font-size:13px;color:#333;border-right:1px solid #bbb}
.search .field{flex:1;padding-left:14px;font-size:12px;color:#999}
.search .go{width:58px;height:58px;border-radius:50%;background:var(--orange);display:flex;align-items:center;justify-content:center;margin-right:2px}

/* destinations strip */
.dest-intro{left:0;top:610px;width:260px;height:200px;background:var(--white)}
.dest-intro h2{position:absolute;left:88px;top:48px}
.dest-intro p{position:absolute;left:88px;top:78px;width:150px;font-size:10px;line-height:15px;color:var(--muted)}
.arrows{display:flex;gap:3px}
.arrow{width:31px;height:30px;background:var(--purple);display:flex;align-items:center;justify-content:center}
.dest-card{top:497px;width:218px;height:313px;overflow:hidden}
.dest-card span{position:absolute;left:24px;top:27px;font-family:"Open Sans",sans-serif;font-weight:800;font-size:15px;color:var(--white);white-space:nowrap}

/* popular */
.sea{left:0;top:972px;width:1200px;height:511px;background:linear-gradient(90deg,#6f8c6c 0%,#b8c2b5 15%,#38b3c1 55%,#1a8ea6 100%)}
.popular{left:169px;top:885px;width:850px;height:457px;background:var(--panel);box-shadow:0 6px 18px rgba(0,0,0,.18)}
.thumb{top:1108px;width:97px;height:87px}
.explore-link{left:894px;top:1297px;display:flex;align-items:center;gap:10px;font-size:11px;color:#444}
.circle-btn{width:31px;height:31px;border-radius:50%;background:var(--purple);display:flex;align-items:center;justify-content:center}

/* offer */
.map{left:0;top:1493px;width:517px;height:500px;background:linear-gradient(135deg,#cfe3f5 0%,#e8f0dd 35%,#bedc9f 60%,#eef0e6 100%)}
.explore-btn{left:939px;top:1898px;width:93px;height:35px;background:var(--orange);color:var(--white);font-size:10.5px;display:flex;align-items:center;justify-content:center;gap:6px;text-transform:uppercase}

/* recommendations */
.grid-tile{position:absolute}

/* reach */
.reach{left:0;top:2889px;width:1200px;height:165px;background:linear-gradient(180deg,#4f8fc9 0%,#a6cbe6 45%,#9a8f7a 75%,#6d8aa8 100%)}
.reach-input{left:302px;top:2986px;width:421px;height:39px;background:var(--white);font-size:10px;color:#aaa;padding:14px 24px}
.reach-btn{left:735px;top:2986px;width:161px;height:39px;background:var(--orange);color:var(--white);font-size:11px;font-family:"Open Sans",sans-serif;font-weight:600;display:flex;align-items:center;justify-content:center;gap:10px}

/* footer */
.footer{left:0;top:3054px;width:1200px;height:189px;background:var(--footer)}
.footer-brand{left:133px;top:3120px;display:flex;align-items:center;gap:10px}
.footer-brand .brand-dot{width:60px;height:60px}
.foot-col{position:absolute;top:3095px}
.foot-col h3{font-family:"Open Sans",sans-serif;font-weight:700;font-size:12.5px;color:var(--footer-dark)}
.foot-col ul{list-style:none;margin-top:24px}
.foot-col li{font-size:10.5px;color:var(--white);height:22.5px;padding-left:18px;position:relative}
.foot-col li::before{content:"›";position:absolute;left:4px;top:-1px;color:rgba(255,255,255,.6)}
.contact-line{margin-top:18px;font-family:"Open Sans",sans-serif;font-weight:600;font-size:12.5px;color:var(--white);white-space:nowrap}
.contact-line span+span{margin-left:14px}
.legal{left:0;top:3243px;width:1200px;height:31px;background:var(--footer-dark);font-size:10px;color:#b8b2dc}
</style>
</head>
<body>

<!-- Hero -->
<section class="abs hero" role="img" aria-label="Night skyline of Dubai with the sail-shaped hotel tower over the water"></section>
<div class="abs brand"><div class="brand-dot"></div><span class="brand-name">Prism Voyages</span></div>
<ul class="abs nav"><li>Home</li><li>About Us</li><li>City Guide</li><li>Blogs</li><li>Contact Us</li></ul>
<div class="abs book">Book Now</div>
<div class="abs search">
  <div class="select">All Destination
    <svg width="9" height="7" viewBox="0 0 9 7"><path d="M0 0h9L4.5 7z" fill="#444"/></svg></div>
  <div class="field">search</div>
  <div class="go"><svg width="34" height="34" viewBox="0 0 34 34" fill="none" stroke="#fff" stroke-width="2.4"><circle cx="18" cy="15" r="11"/><path d="M10 23l-6 7"/></svg></div>
</div>

<!-- Destinations -->
<div class="abs dest-intro">
  <h2>Destinations</h2>
  <p>Lorem ipsum dolor sit amet, consectetur adipiscing elitquisque tempus ac eget diam et laoreet phasellus.</p>
  <div class="abs arrows" style="left:184px;top:168px">
    <div class="arrow"><svg width="12" height="10" viewBox="0 0 12 10" fill="none" stroke="#fff" stroke-width="1.5"><path d="M12 5H1M5 1L1 5l4 4"/></svg></div>
    <div class="arrow"><svg width="12" height="10" viewBox="0 0 12 10" fill="none" stroke="#fff" stroke-width="1.5"><path d="M0 5h11M7 1l4 4-4 4"/></svg></div>
  </div>
</div>
<div class="photo dest-card" style="left:260px;background:linear-gradient(180deg,#5d8fd0,#b8cfe6 60%,#6fb6c5)" role="img" aria-label="Dubai sail-shaped hotel tower against blue sky"><span>DUBAI</span></div>
<div class="photo dest-card" style="left:478px;background:linear-gradient(180deg,#3f7fc8,#9bbad6 55%,#3d7f8e)" role="img" aria-label="Abu Dhabi towers reflected in a marina"><span>ABU DHABI</span></div>
<div class="photo dest-card" style="left:696px;background:linear-gradient(180deg,#3f8fd6,#c9b89a 55%,#5e9a4c)" role="img" aria-label="Ras Al Khaimah resort with golf course"><span>RAS AL KHAIMAH</span></div>
<div class="photo dest-card" style="left:914px;background:linear-gradient(180deg,#6fa8d8,#c9d3d8 55%,#6a7a5e)" role="img" aria-label="Sharjah waterfront skyline and highway"><span>SHARJAH</span></div>
<div class="photo dest-card" style="left:1132px;width:68px;background:linear-gradient(180deg,#c9d5e2,#c8a27a)" role="img" aria-label="Fujairah camel in the desert"><span>FUJAIRAH</span></div>

<!-- Popular destinations -->
<div class="photo sea" role="img" aria-label="Aerial view of a beach with turquoise sea and resort buildings"></div>
<section class="abs popular">
  <div class="photo" style="left:0;top:0;width:334px;height:457px;background:linear-gradient(180deg,#aac6de,#d8dcd6 45%,#8a9a78)" role="img" aria-label="Palm-lined walkway leading to the sea"></div>
  <h2 class="abs" style="left:390px;top:56px">The Most Popular Travel Destinations</h2>
  <p class="abs body" style="left:390px;top:92px;width:412px">Ubique iudicabit aliquando ex vix. Sea vidit mucius ei, his cu nihil legendos. Per nonumes posidonium ex. Vel possim contentiones no, qui te singulis laboramus dissentiunt. Ea vix sanctus ullamcorper.</p>
  <div class="abs arrows" style="left:306px;top:405px">
    <div class="arrow"><svg width="12" height="10" viewBox="0 0 12 10" fill="none" stroke="#fff" stroke-width="1.5"><path d="M12 5H1M5 1L1 5l4 4"/></svg></div>
    <div class="arrow"><svg width="12" height="10" viewBox="0 0 12 10" fill="none" stroke="#fff" stroke-width="1.5"><path d="M0 5h11M7 1l4 4-4 4"/></svg></div>
  </div>
</section>
<div class="photo thumb" style="left:559px;background:linear-gradient(180deg,#e9ddd0,#8a6a55)" role="img" aria-label="Street food cart"></div>
<div class="photo thumb" style="left:666px;background:linear-gradient(180deg,#4f86c6,#d2c4a8)" role="img" aria-label="Beach hotel with sun loungers"></div>
<div class="photo thumb" style="left:773px;background:linear-gradient(180deg,#3f7fd0,#3aa0b5)" role="img" aria-label="Resort marina with palm trees"></div>
<div class="photo thumb" style="left:878px;background:linear-gradient(180deg,#7fb8e6,#e0c8a8)" role="img" aria-label="Couple running on the beach"></div>
<div class="abs explore-link">Explore<div class="circle-btn"><svg width="8" height="10" viewBox="0 0 8 10" fill="none" stroke="#fff" stroke-width="1.6"><path d="M2 1l4 4-4 4"/></svg></div></div>

<!-- Travel offer -->
<div class="photo map" role="img" aria-label="Road map of the region with destination clusters"></div>
<h2 class="abs" style="left:595px;top:1544px">Our Travel Offer</h2>
<p class="abs body" style="left:595px;top:1578px;width:420px">Ubique iudicabit aliquando ex vix. Sea vidit mucius ei, his cu nihil legendos. Per nonumes posidonium ex. Vel possim contentiones no, qui te singulis laboramus dissentiunt. Ea vix sanctus ullamcorper.</p>
<div class="photo" style="left:519px;top:1659px;width:364px;height:333px;background:linear-gradient(180deg,#c8dcef,#6e8c58 50%,#2f4f7a 75%,#b7aa96);box-shadow:0 4px 12px rgba(0,0,0,.2)" role="img" aria-label="Resort pool lined with palm trees"></div>
<p class="abs body" style="left:939px;top:1762px;width:160px">Ubique iudicabit aliquando ex vix. Sea vidit mucius ei, his cu nihil legendos.</p>
<div class="abs explore-btn"><svg width="13" height="13" viewBox="0 0 13 13" fill="none" stroke="#fff" stroke-width="1.2"><circle cx="6.5" cy="6.5" r="5.5"/><path d="M9 4L5.5 5.5 4 9l3.5-1.5z"/></svg>Explore</div>

<!-- Recommendations -->
<h2 class="abs" style="left:0;top:2073px;width:1200px;text-align:center">Our Recommendations for Dubai</h2>
<p class="abs body" style="left:390px;top:2104px;width:420px;text-align:center">Ubique iudicabit aliquando ex vix. Sea vidit mucius ei, his cu nihil legendos. Per nonumes posidonium ex. Vel possim contentiones no, qui te singulis laboramus dissentiunt. Ea vix sanctus ullamcorper.</p>

<div class="grid-tile" style="left:75px;top:2208px;width:273px;height:248px;background:linear-gradient(180deg,#a9c6de,#6f8ea8 60%,#3d6a86)" role="img" aria-label="Abu Dhabi skyline by the sea"></div>
<div class="grid-tile" style="left:75px;top:2467px;width:273px;height:248px;background:linear-gradient(180deg,#4e86c8,#dfe6ee 60%,#8a9a88)" role="img" aria-label="White grand mosque with minarets"></div>
<div class="grid-tile" style="left:75px;top:2724px;width:273px;height:140px;background:linear-gradient(180deg,#f1d9a8,#d98a3a)" role="img" aria-label="Desert dunes with four-wheel drives"></div>

<div class="grid-tile" style="left:357px;top:2208px;width:272px;height:193px;background:linear-gradient(180deg,#2c3a66,#a0602a 60%,#2a2a3a)" role="img" aria-label="Palm resort hotel lit at dusk"></div>
<div class="grid-tile" style="left:357px;top:2411px;width:272px;height:215px;background:linear-gradient(180deg,#8eb2e2,#e6dccb)" role="img" aria-label="Mosque domes and minaret"></div>
<div class="grid-tile" style="left:357px;top:2635px;width:272px;height:229px;background:linear-gradient(180deg,#e8b070,#c45a1e)" role="img" aria-label="Car dune bashing in the desert"></div>

<div class="grid-tile" style="left:638px;top:2208px;width:203px;height:452px;background:linear-gradient(180deg,#1f5ea8,#8eb7df 70%,#5a6a6a)" role="img" aria-label="Tall Dubai skyscraper"></div>
<div class="grid-tile" style="left:638px;top:2669px;width:203px;height:195px;background:linear-gradient(180deg,#d8dde0,#c9a98a)" role="img" aria-label="Falconer with a falcon in the desert"></div>

<div class="grid-tile" style="left:850px;top:2208px;width:274px;height:248px;background:linear-gradient(180deg,#f1f3f5,#e1d2b8 70%,#b89874)" role="img" aria-label="Camels with riders in the desert"></div>
<div class="grid-tile" style="left:850px;top:2467px;width:274px;height:397px;background:linear-gradient(180deg,#9ab6d6,#4a6a8a 60%,#5a7a52)" role="img" aria-label="Sharjah glass towers and street lamps"></div>

<!-- Reach to us -->
<section class="abs reach" role="img" aria-label="Coastal city panorama under a blue sky"></section>
<h2 class="abs" style="left:302px;top:2933px">Reach to Us</h2>
<p class="abs" style="left:306px;top:2958px;font-size:10.5px;color:#222">Describe us what is your requirement, we will plan for you...!</p>
<div class="abs reach-input">tell us</div>
<div class="abs reach-btn"><svg width="20" height="15" viewBox="0 0 20 15"><rect width="20" height="15" rx="1.5" fill="#fff"/><path d="M1 1.5l9 7 9-7" fill="none" stroke="#f08a24" stroke-width="1.6"/></svg>SUBSSCRIBE</div>

<!-- Footer -->
<footer class="abs footer"></footer>
<div class="abs footer-brand"><div class="brand-dot"></div><span class="brand-name" style="color:var(--footer-dark)">Prism Voyages</span></div>
<div class="foot-col" style="left:435px">
  <h3>Quick Link</h3>
  <ul><li>HOME</li><li>ABOUT US</li><li>CITY GUIDE</li><li>BLOG</li><li>FAQ's</li></ul>
</div>
<div class="foot-col" style="left:628px">
  <h3>Get In Touch</h3>
  <ul><li>Newsletter</li><li>Journal</li><li>Gallery</li><li>Videos</li></ul>
</div>
<div class="foot-col" style="left:858px;width:320px">
  <h3>CONTACT US</h3>
  <p style="margin-top:24px;width:250px;font-size:10.5px;line-height:18px;color:var(--white)">Feel free to get in touch with us via phone or send us a message</p>
  <p class="contact-line"><span>+1 800 555 0199</span><span>hello@prismvoyages.example</span></p>
</div>
<div class="abs legal">
  <span class="abs" style="left:129px;top:10px">@ Copyright 2021. All Right Reserved</span>
  <span class="abs" style="left:876px;top:10px">Privacy Policy</span>
  <span class="abs" style="left:972px;top:10px">Terms &amp; Conditions</span>
</div>

</body>
</html>
```